Stationary Design Letterhead and Envelope

Artist should provide Letterhead and envelop stationary designs

Info for stationary:
Fenwarde Outdoor Advertising
4857 Mesa Rd. 318 N. PO BOX 582917
Austin, TX 78651

Dale Fenwarde
President
512-608-2917
dale@fenwardeoutdoor.example
fenwardeoutdoor.example

Target Market(s)

clients

Colors
0054AA
0677BA
7BADD7
CADEEF
E8F1F8

Requirements
Must have
• high quality unique eye catching and dynamic

```html
<!DOCTYPE html>
<html lang="en">
<head>
<meta charset="utf-8">
<title>Fenwarde Outdoor Advertising Stationery</title>
<link href="https://fonts.googleapis.com/css2?family=Lato:wght@400;700&family=Open+Sans:wght@400;500&display=swap" rel="stylesheet">
<style>
  :root {
    --brand-blue: #0054AA;
    --accent-blue: #0677BA;
    --ink: #0a0a0c;
    --text: #4a4a4a;
    --paper: #ffffff;
    --backdrop: #e6e7e9;
  }
  * { box-sizing: border-box; margin: 0; padding: 0; }
  html, body { width: 1200px; height: 1200px; overflow: hidden; }
  body { background: var(--backdrop); position: relative; font-family: 'Open Sans', sans-serif; }

  .letterhead {
    position: absolute; left: 50px; top: 214px; width: 600px; height: 772px;
    background: var(--paper); box-shadow: 0 4px 18px rgba(0,0,0,.18); overflow: hidden;
  }
  .brand-name {
    position: absolute; display: flex; align-items: center;
    font-family: 'Lato', sans-serif; font-weight: 700; color: var(--ink);
    text-transform: uppercase;
  }
  .brand-name::before { content: ""; flex: none; background: var(--brand-blue); }
  .letterhead .brand-name { left: 56px; top: 32px; width: 220px; gap: 10px; font-size: 17px; line-height: 21px; }
  .letterhead .brand-name::before { width: 30px; height: 30px; }

  .contact { position: absolute; left: 359px; top: 12px; padding-left: 14px; border-left: 1.5px solid #555; height: 72px; font-family: 'Lato', sans-serif; }
  .contact-name { color: var(--brand-blue); font-weight: 700; font-size: 14px; text-transform: uppercase; line-height: 1; }
  .contact-role { font-size: 11.5px; color: #222; margin: 1px 0 6px; }
  .contact-line { display: flex; align-items: center; gap: 6px; font-size: 11.5px; color: #222; line-height: 14px; }
  .contact-line svg { width: 10px; height: 10px; fill: var(--brand-blue); flex: none; }

  .letter-body { position: absolute; left: 56px; top: 138px; width: 486px; font-size: 9.6px; color: var(--text); }
  .letter-body p { margin-bottom: 16px; line-height: 17.3px; text-align: justify; }
  .letter-body .meta { line-height: 11.5px; }
  .signature-mark { width: 140px; height: 16px; margin: -2px 0 8px; background: linear-gradient(90deg, rgba(60,60,60,.25), rgba(60,60,60,.08)); border-radius: 8px; }
  .signer-name { font-size: 12px; color: #222; font-weight: 500; margin-bottom: 3px; }

  .footer-wave { position: absolute; left: 0; bottom: 0; width: 100%; }
  .footer-address { position: absolute; right: 64px; text-align: right; font-family: 'Lato', sans-serif; color: #fff; }
  .letterhead .footer-address { bottom: 22px; font-size: 11.5px; line-height: 14px; }
  .footer-company { color: var(--accent-blue); text-transform: uppercase; }

  .envelope { position: absolute; left: 705px; width: 465px; height: 232px; background: var(--paper); box-shadow: 0 4px 14px rgba(0,0,0,.18); overflow: hidden; }
  .envelope-front { top: 455px; }
  .envelope-front .brand-name { left: 37px; top: 28px; width: 170px; gap: 7px; font-size: 12.5px; line-height: 15px; }
  .envelope-front .brand-name::before { width: 22px; height: 22px; }
  .envelope-front .footer-address { right: 35px; bottom: 11px; font-size: 8.2px; line-height: 10.5px; }
  .envelope-back { top: 746px; height: 228px; box-shadow: 0 3px 10px rgba(0,0,0,.12); }
  .envelope-flap { position: absolute; left: 0; top: 0; width: 100%; height: 55px; }
</style>
</head>
<body>

<section class="letterhead">
  <div class="brand-name"><span>Fenwarde Outdoor Advertising</span></div>

  <div class="contact">
    <div class="contact-name">Dale Fenwarde</div>
    <div class="contact-role">President</div>
    <div class="contact-line"><svg viewBox="0 0 10 10"><path d="M1 3 Q5 0 9 3 L8 4.5 L6.5 3.8 V3 H3.5 V3.8 L2 4.5 Z M2.5 5 H7.5 L8.5 9 H1.5 Z"/></svg>512-608-2917</div>
    <div class="contact-line"><svg viewBox="0 0 10 10"><path d="M0.5 2 H9.5 V8 H0.5 Z M1 2.5 L5 5.5 L9 2.5" stroke="#fff" stroke-width=".8"/></svg>dale@fenwardeoutdoor.example</div>
    <div class="contact-line"><svg viewBox="0 0 10 10"><circle cx="5" cy="5" r="4.5"/><path d="M3 3.5 L5 3 L5.5 5 L4 6.5 M6.5 7 L7.5 5.5" stroke="#fff" stroke-width=".8" fill="none"/></svg>fenwardeoutdoor.example</div>
  </div>

  <div class="letter-body">
    <p class="meta">Issuing Date: May 5, 2018</p>
    <p class="meta" style="margin-bottom:34px">Name Of Employee Mr. XYZABC<br>Address of Employee<br>Address Line 2 etc..</p>
    <p class="meta" style="margin-bottom:28px">Dear Mr.XYZABC</p>
    <p>Lorem Ipsum has been the industry's standard dummy text ever since the 1500s, when an unknown printer took a galley of type and scrambled it to make a type specimen book. It has survived not only five centuries, but also the leap into electronic typesetting, remaining essentially unchanged. It was popularised in the 1960s with the release of Typeline sheets containing Lorem Ipsum passages, and more recently with desktop publishing software like Quillset Layout including versions of Lorem Ipsum.</p>
    <p>Lorem Ipsum is simply dummy text of the printing and typesetting industry. Lorem Ipsum has been the industry's standard dummy text ever since the 1500s, when an unknown printer took a galley of type and scrambled it to make a type specimen book.</p>
    <p style="margin-bottom:40px">It has survived not only five centuries, but also the leap into electronic typesetting, remaining essentially unchanged. It was popularised in the 1960s with the release of Typeline sheets containing Lorem IpsumIpsum passages.</p>
    <p class="meta" style="margin-bottom:10px">Yours Sincerely</p>
    <div class="signature-mark" role="img" aria-label="Handwritten signature of Marcus Ellery"></div>
    <div class="signer-name">Marcus Ellery</div>
    <p class="meta">Managing Director</p>
  </div>

  <svg class="footer-wave" width="600" height="106" viewBox="0 0 600 106" aria-hidden="true">
    <path d="M0 0 C90 38 200 58 290 50 C320 47 340 42 360 36 C250 62 110 60 0 26 Z" fill="var(--accent-blue)"/>
    <path d="M0 30 C120 66 240 68 360 38 C450 18 530 8 600 10 V106 H0 Z" fill="var(--ink)"/>
    <path d="M0 28 C120 64 240 66 360 36" stroke="#fff" stroke-width="2" fill="none"/>
  </svg>
  <div class="footer-address">
    <div class="footer-company">Fenwarde Outdoor Advertising</div>
    <div>4857 Mesa Rd. 318 N. PO BOX 582917</div>
    <div>Austin, TX 78651</div>
  </div>
</section>

<section class="envelope envelope-front">
  <div class="brand-name"><span>Fenwarde Outdoor Advertising</span></div>
  <svg class="footer-wave" width="465" height="62" viewBox="0 0 465 62" aria-hidden="true">
    <path d="M0 0 C70 24 150 34 210 30 C230 28 240 25 245 24 C170 40 80 38 0 16 Z" fill="var(--accent-blue)"/>
    <path d="M0 18 C90 42 170 42 245 25 C320 8 400 0 465 2 V62 H0 Z" fill="var(--ink)"/>
    <path d="M0 17 C90 41 170 41 245 24" stroke="#fff" stroke-width="1.5" fill="none"/>
  </svg>
  <div class="footer-address">
    <div class="footer-company">Fenwarde Outdoor Advertising</div>
    <div>4857 Mesa Rd. 318 N. PO BOX 582917, Austin, TX 78651</div>
  </div>
</section>

<section class="envelope envelope-back">
  <svg class="envelope-flap" width="465" height="55" viewBox="0 0 465 55" aria-hidden="true">
    <path d="M0 0 H465 L445 55 H18 Z" fill="var(--ink)"/>
  </svg>
</section>

</body>
</html>
```